business card for larch cove dental arts
Larch Cove Dental Arts
Professional
Rowland K. Bevacquist DDS
4 Mossbank Ln
Larch Cove, NY 14093
larchcovedentalarts@mailvane.example
larchcovedentalarts.example
On the card either at the bottom or the top I would like it to say "Implants Family Dentistry Cosmetic Dentistry" to tell people what i offer, or as a motto
________ ______ has an appointment
___/___/___@ ___:___am/pm
Mon Tues Wed Thurs Fri Sat
Logo design
the white may be easier to work with for the card

```html
<!DOCTYPE html>
<html lang="en">
<head>
<meta charset="utf-8">
<title>Larch Cove Dental Arts — Stationery</title>
<link href="https://fonts.googleapis.com/css2?family=Cinzel:wght@500&family=Lato:wght@400;700&display=swap" rel="stylesheet">
<style>
  :root{
    --backdrop:#e6e4e1;
    --paper:#ffffff;
    --ink:#111111;
    --grey:#8a8a8a;
    --soft-grey:#c9c9c9;
    --faint:#efefef;
    --label:#4a4a4a;
  }
  *{box-sizing:border-box;margin:0;padding:0}
  html,body{width:1200px;height:434px;overflow:hidden}
  body{background:var(--backdrop);position:relative;font-family:"Lato",Arial,sans-serif;color:var(--ink)}
  .sheet{position:absolute;background:var(--paper);box-shadow:0 2px 6px rgba(0,0,0,.25);overflow:hidden}
  .letterhead{top:24px;width:228px;height:372px}
  .opt-1{left:24px}.opt-2{left:290px}.opt-3{left:559px}
  .brand{position:absolute;left:0;right:0;text-align:center;font-family:"Cinzel",Georgia,serif;font-weight:500;color:var(--ink);line-height:1.15}
  .brand .dot{display:block;margin:0 auto 3px;border-radius:50%;background:var(--ink)}
  .letterhead .brand{top:16px;font-size:7.5px;letter-spacing:.4px}
  .letterhead .brand .dot{width:14px;height:14px}
  .faint-mark{position:absolute;left:24px;top:150px;width:110px;height:110px;border-radius:50%;background:var(--faint)}
  .art-area{position:absolute;left:70px;top:60px;width:110px;height:150px;border-radius:40% 50% 45% 55%;
    background:radial-gradient(circle at 40% 45%,#d8dbe6 0%,#eceaf0 55%,rgba(255,255,255,0) 75%)}
  .foot-line{position:absolute;left:10px;right:10px;bottom:14px;font-size:3.6px;color:var(--grey);text-align:left;white-space:nowrap}
  .swoosh{position:absolute;left:0;bottom:0;width:100%}
  .swoosh-text{position:absolute;left:8px;bottom:6px;font-size:3.6px;color:#dcdcdc;white-space:nowrap}
  .fax-title{position:absolute;left:12px;top:66px;font-size:13px;font-weight:700;letter-spacing:.5px}
  .fax-fields{position:absolute;left:12px;right:12px;top:86px;display:grid;grid-template-columns:1fr 1fr;column-gap:10px;row-gap:6px;font-size:4px;color:var(--label)}
  .fax-fields span{border-bottom:.6px solid var(--soft-grey);padding-bottom:1px}
  .fax-checks{position:absolute;left:12px;right:12px;top:132px;display:flex;justify-content:space-between;font-size:3.6px;color:var(--label)}
  .fax-checks span::before{content:"";display:inline-block;width:4px;height:4px;border:.6px solid var(--grey);margin-right:2px;vertical-align:-1px}
  .fax-rule{position:absolute;left:12px;right:12px;top:142px;border-top:.6px solid var(--soft-grey)}
  .label{position:absolute;top:404px;font-size:10px;color:var(--label);width:228px;text-align:center}
  .envelope-back{left:852px;top:26px;width:336px;height:170px}
  .envelope-front{left:832px;top:92px;width:340px;height:176px}
  .envelope-front .brand{left:12px;right:auto;top:12px;font-size:7px;text-align:center;width:80px}
  .envelope-front .brand .dot{width:13px;height:13px}
  .envelope-front .return{position:absolute;left:12px;top:50px;font-size:3.6px;color:var(--grey);line-height:1.4}
  .card{top:343px;height:66px}
  .card-front{left:852px;width:146px}
  .card-back{left:1008px;width:168px}
  .card-front .brand{top:8px;font-size:5.4px}
  .card-front .brand .dot{width:10px;height:10px;margin-bottom:2px}
  .card-back .brand{left:auto;right:8px;top:6px;width:52px;font-size:4px}
  .card-back .brand .dot{width:7px;height:7px}
  .appointment{position:absolute;left:8px;top:7px;font-size:3.6px;line-height:1.7;color:var(--label)}
  .appointment strong{font-size:4px;color:var(--ink)}
  .services{position:absolute;left:0;right:0;bottom:3px;text-align:center;font-size:3.4px;color:#e4e4e4;letter-spacing:.2px}
</style>
</head>
<body>

  <!-- Letterhead, option 1 -->
  <section class="sheet letterhead opt-1">
    <div class="brand"><span class="dot"></span>LARCH COVE<br>DENTAL ARTS</div>
    <div class="faint-mark"></div>
    <p class="foot-line">4 Mossbank Ln · Larch Cove, NY 14093 · larchcovedentalarts@mailvane.example · larchcovedentalarts.example</p>
  </section>
  <p class="label" style="left:24px">Option-1</p>

  <!-- Letterhead, option 2 -->
  <section class="sheet letterhead opt-2">
    <div class="brand"><span class="dot"></span>LARCH COVE<br>DENTAL ARTS</div>
    <div class="art-area" role="img" aria-label="Soft illustration of a paint palette with a brush"></div>
    <svg class="swoosh" viewBox="0 0 228 80" width="228" height="80" aria-hidden="true">
      <path d="M0,80 L0,52 C70,78 150,62 228,8 L228,80 Z" fill="#111"/>
      <path d="M0,46 C70,72 150,56 228,2" fill="none" stroke="#9a9a9a" stroke-width="2"/>
    </svg>
    <p class="swoosh-text">4 Mossbank Ln · Larch Cove, NY 14093 · larchcovedentalarts.example</p>
  </section>
  <p class="label" style="left:290px">Option-2</p>

  <!-- Fax sheet, option 3 -->
  <section class="sheet letterhead opt-3">
    <div class="brand"><span class="dot"></span>LARCH COVE<br>DENTAL ARTS</div>
    <h2 class="fax-title">FAX</h2>
    <div class="fax-fields">
      <span>To:</span><span>From:</span>
      <span>Fax:</span><span>Pages:</span>
      <span>Phone:</span><span>Date:</span>
      <span>Re:</span><span>CC:</span>
    </div>
    <div class="fax-checks"><span>Urgent</span><span>Review</span><span>Comment</span><span>Reply</span><span>Recycle</span></div>
    <div class="fax-rule"></div>
    <svg class="swoosh" viewBox="0 0 228 80" width="228" height="80" aria-hidden="true">
      <path d="M0,80 L0,52 C70,78 150,62 228,8 L228,80 Z" fill="#111"/>
      <path d="M0,46 C70,72 150,56 228,2" fill="none" stroke="#9a9a9a" stroke-width="2"/>
    </svg>
    <p class="swoosh-text">4 Mossbank Ln · Larch Cove, NY 14093 · larchcovedentalarts.example</p>
  </section>
  <p class="label" style="left:559px">Option-3</p>

  <!-- Envelope, back -->
  <section class="sheet envelope-back">
    <svg viewBox="0 0 336 170" width="336" height="170" aria-hidden="true">
      <path d="M0,0 H336 V30 C240,40 200,70 168,96 C130,70 90,40 0,30 Z" fill="#111"/>
      <path d="M0,36 C90,46 130,76 168,102 C200,76 240,46 336,36" fill="none" stroke="#9a9a9a" stroke-width="1.5"/>
    </svg>
  </section>

  <!-- Envelope, front -->
  <section class="sheet envelope-front">
    <div class="brand"><span class="dot"></span>LARCH COVE<br>DENTAL ARTS</div>
    <p class="return">4 Mossbank Ln<br>Larch Cove, NY 14093</p>
    <svg class="swoosh" viewBox="0 0 340 60" width="340" height="60" aria-hidden="true">
      <path d="M0,60 L0,48 C120,60 250,50 340,10 L340,60 Z" fill="#111"/>
      <path d="M0,43 C120,55 250,45 340,4" fill="none" stroke="#9a9a9a" stroke-width="1.5"/>
    </svg>
  </section>

  <!-- Business card, front -->
  <section class="sheet card card-front">
    <div class="brand"><span class="dot"></span>LARCH COVE<br>DENTAL ARTS</div>
    <svg class="swoosh" viewBox="0 0 146 26" width="146" height="26" aria-hidden="true">
      <path d="M0,26 L0,14 C50,24 100,18 146,2 L146,26 Z" fill="#111"/>
      <path d="M0,11 C50,21 100,15 146,0" fill="none" stroke="#9a9a9a" stroke-width="1"/>
    </svg>
    <p class="services">Implants · Family Dentistry · Cosmetic Dentistry</p>
  </section>

  <!-- Business card, back -->
  <section class="sheet card card-back">
    <div class="appointment">
      <strong>Rowland K. Bevacquist DDS</strong><br>
      ________ ______ has an appointment<br>
      ___/___/___ @ ___:___ am/pm<br>
      Mon Tues Wed Thurs Fri Sat
    </div>
    <div class="brand"><span class="dot"></span>LARCH COVE<br>DENTAL ARTS</div>
    <svg class="swoosh" viewBox="0 0 168 22" width="168" height="22" aria-hidden="true">
      <path d="M0,22 L0,14 C60,22 120,16 168,2 L168,22 Z" fill="#111"/>
      <path d="M0,11 C60,19 120,13 168,0" fill="none" stroke="#9a9a9a" stroke-width="1"/>
    </svg>
  </section>

</body>
</html>
```